Northwind Trade Allies - Letterhead and Folder

I am looking for letterhead that uses the splash from the logo on the side of the page as well as some information from our website.

I am looking for a folder that is a fold out that has pockets to hold paper as well as a slits for a business card.

Website address is www.northwindtradeallies.example

Target Market(s)

Export of Agrifoods, commodities and emergency aid.
Supplying the world food security.

Requirements
Must have
• Use splash and logo, have information about company.
• Letterhead must have splash on a side not in the middle.
Nice to have
• Different pictures that what are provided.

```html
<!DOCTYPE html>
<html lang="en">
<head>
<meta charset="utf-8">
<title>Northwind Trade Allies – Letterhead</title>
<link rel="stylesheet" href="https://fonts.googleapis.com/css2?family=Montserrat:wght@400;600&display=swap">
<style>
  :root{
    --backdrop:#ececec;
    --paper:#ffffff;
    --ink:#3a3a3a;
    --brand-dark:#3f9a3c;
    --brand-lime:#93bf2a;
    --brand-mist:#e4ece6;
    --brand-sky:#d3e2e6;
  }
  *{box-sizing:border-box;margin:0;padding:0}
  html,body{width:1200px;height:795px;overflow:hidden;background:var(--backdrop)}
  body{font-family:"Montserrat",Arial,sans-serif;color:var(--ink);position:relative}
  .letterhead{
    position:absolute;left:338px;top:28px;width:524px;height:740px;
    background:var(--paper);box-shadow:0 6px 18px rgba(0,0,0,.12);overflow:hidden;
  }
  .brand{position:absolute;left:52px;top:56px;display:flex;align-items:center;gap:10px}
  .brand-dot{width:26px;height:26px;border-radius:50%;background:var(--brand-dark)}
  .brand-name{font-size:12px;font-weight:600;letter-spacing:.1em;text-transform:uppercase;color:var(--ink)}
  .splash{position:absolute;right:0;top:330px;width:190px;height:300px}
  .contact{position:absolute;left:52px;bottom:46px;font-size:8.5px;line-height:1.55}
  .contact-address{margin-bottom:9px;font-style:normal}
  .contact-list{list-style:none}
  .contact-list li{display:flex;align-items:center;gap:7px}
  .contact-list svg{width:8px;height:8px;fill:none;stroke:var(--brand-dark);stroke-width:1.4}
</style>
</head>
<body>
  <main class="letterhead">
    <header class="brand">
      <span class="brand-dot"></span>
      <span class="brand-name">Northwind Trade Allies</span>
    </header>

    <svg class="splash" viewBox="0 0 190 300" role="img" aria-label="Brand splash decoration in soft greens and sky blue curving in from the page edge">
      <defs>
        <radialGradient id="splashTone" cx="190" cy="150" r="150" gradientUnits="userSpaceOnUse">
          <stop offset="0" stop-color="var(--brand-dark)"/>
          <stop offset=".4" stop-color="var(--brand-lime)"/>
          <stop offset=".75" stop-color="var(--brand-sky)"/>
          <stop offset="1" stop-color="var(--brand-mist)"/>
        </radialGradient>
      </defs>
      <path d="M190 0 A150 150 0 0 0 190 300 Z" fill="url(#splashTone)"/>
    </svg>

    <footer class="contact">
      <address class="contact-address">
        Suite 12, 8 Harbour Lane<br>Millbrook Quay<br>Eastport EP4 2QT
      </address>
      <ul class="contact-list">
        <li><svg viewBox="0 0 10 10"><path d="M2 1h2l1 2-1 1a5 5 0 0 0 2 2l1-1 2 1v2a1 1 0 0 1-1 1A7 7 0 0 1 1 2a1 1 0 0 1 1-1z"/></svg>+44 (0)100 555 0142</li>
        <li><svg viewBox="0 0 10 10"><rect x="2.5" y="1" width="5" height="8" rx="1"/></svg>+44 (0)7700 900 318</li>
        <li><svg viewBox="0 0 10 10"><rect x="1" y="2" width="8" height="6"/><path d="M1 2l4 3 4-3"/></svg>jon@northwindtradeallies.example</li>
        <li><svg viewBox="0 0 10 10"><circle cx="5" cy="5" r="4"/><path d="M1 5h8M5 1c2 2 2 6 0 8M5 1c-2 2-2 6 0 8"/></svg>www.northwindtradeallies.example</li>
      </ul>
    </footer>
  </main>
</body>
</html>
```